Construction Company - Aluminum Welding Substations - 8 page Brochure

See attached for very rough idea of brochure idea and general idea - primary goal is to highlight various services provided as unique for our industry.

- About Us - see website (brevoforge.com) & Company Resume

- Why Welded Fittings - see PPT & language in comments

- Services Provided - See categories broke out on website - highlight Aluminum Bus Welding, Bus Bending, All Weather Welding, Field Fabrication.

- Contact Page - see website

- Want to use as many photo's to highlight work as possible as people like to see the finished product of the substation/bus bending
Updates

Target Market(s)

General Contractors - we are Specialty Subcontractor

Industry/Entity Type

Construction - Welding Substations

Font styles to use
Serif
Sans Serif

Colors
0054AA
0677BA
7BADD7
CADEEF
E8F1F8
0094D4
00A9DD
6FCCEA
C7EBF8
E9F6FB
F0912C
F2A743
F7CA91
FBE8D2
FDF5EE

Requirements
Must have
• Logo, "Quality Craftsmanship without Compromise", Services Provided, as many pictures as makes sense to highlight work

```html
<!DOCTYPE html>
<html lang="en">
<head>
<meta charset="utf-8">
<title>Why Us – Quellmark Metalworks</title>
<link href="https://fonts.googleapis.com/css2?family=Arimo:wght@400&family=Open+Sans:wght@400;700&display=swap" rel="stylesheet">
<style>
  :root {
    --brand-blue: #0054AA;
    --deep-blue: #004a98;
    --white: #ffffff;
    --photo-grey-light: #b9bcbf;
    --photo-grey-dark: #6d6e6f;
    --photo-steel: #cfd3d6;
  }
  * { box-sizing: border-box; margin: 0; padding: 0; }
  html, body { width: 848px; height: 1200px; overflow: hidden; background: var(--white); }
  .page {
    position: relative; width: 848px; height: 1200px; overflow: hidden;
    font-family: "Open Sans", sans-serif; color: var(--white);
    background: var(--brand-blue);
  }
  .photo-band-top {
    position: absolute; left: 0; top: 0; width: 848px; height: 178px;
    background: linear-gradient(180deg, var(--photo-grey-light), var(--photo-grey-dark));
  }
  .photo-band-bottom {
    position: absolute; left: 0; top: 892px; width: 848px; height: 308px;
    background: linear-gradient(160deg, #8a8b8c 0%, var(--photo-steel) 45%, #7b7c7e 100%);
  }
  .corner-white { position: absolute; left: 0; top: 0; }
  .arc { position: absolute; left: 0; top: 0; }
  .logo-tab {
    position: absolute; left: 83px; top: 0; width: 193px; height: 234px;
    background: var(--brand-blue);
    border-radius: 0 0 96px 96px;
  }
  .logo-name {
    position: absolute; left: 0; right: 0; top: 100px;
    font-weight: 400; font-size: 18px; line-height: 1.3;
    text-align: center; color: var(--white);
  }
  .headline {
    position: absolute; left: 118px; top: 257px;
    font-family: "Arimo", sans-serif; font-weight: 400; font-size: 71px; line-height: 1;
  }
  .section-title {
    position: absolute; font-weight: 700; font-size: 29px; line-height: 1;
  }
  .section-title.aluminum { left: 121px; top: 366px; }
  .section-title.steel { left: 277px; top: 616px; }
  .feature-list {
    position: absolute; list-style: none; font-size: 22.5px; line-height: 33.3px;
    letter-spacing: 0.2px;
  }
  .feature-list li { position: relative; padding-left: 23px; }
  .feature-list li::before {
    content: ""; position: absolute; left: 0; top: 14px;
    width: 7px; height: 7px; border-radius: 50%; background: var(--white);
  }
  .feature-list.aluminum { left: 136px; top: 413px; width: 392px; }
  .feature-list.steel { left: 293px; top: 663px; width: 440px; }
  .diamond {
    position: absolute; border: 7px solid var(--white); border-radius: 36px;
    transform: rotate(45deg); overflow: hidden;
  }
  .diamond.shadowed { box-shadow: -5px 5px 0 var(--deep-blue); }
  .diamond.shop {
    left: 467px; top: 81px; width: 248px; height: 248px;
    background: linear-gradient(135deg, #b8b09c, #7f9aa8 60%, #d9d2bb);
  }
  .diamond.lineman {
    left: 616px; top: 317px; width: 267px; height: 267px;
    background: linear-gradient(135deg, #9a9c98, #c8e24a 55%, #5e625f);
  }
  .diamond.field {
    left: -99px; top: 695px; width: 338px; height: 338px;
    background: linear-gradient(135deg, #8fa7c0, #3f8f80 55%, #5a5c60);
  }
  .diamond.bus-joint {
    left: 182px; top: 970px; width: 247px; height: 247px;
    background: linear-gradient(135deg, #e6e8ea, #bfc4c8 60%, #9ea3a7);
  }
  .web-pill {
    position: absolute; left: 467px; top: 1026px; width: 400px; height: 71px;
    background: var(--white); border-radius: 36px 0 0 36px;
    display: flex; align-items: center; padding-left: 23px; gap: 15px;
  }
  .web-pill span { color: var(--brand-blue); font-size: 19.5px; }
</style>
</head>
<body>
<main class="page">
  <div class="photo-band-top" role="img" aria-label="Aluminum bus pipes on a gravel substation yard"></div>
  <svg class="corner-white" width="848" height="300" aria-hidden="true">
    <polygon points="672,0 848,0 848,285" fill="#ffffff"/>
  </svg>
  <div class="photo-band-bottom" role="img" aria-label="Welded aluminum bus structure with support fittings"></div>
  <svg class="arc" width="848" height="500" aria-hidden="true">
    <path d="M0,178 A380,380 0 0 0 640,370" fill="none" stroke="#2a6cbc" stroke-width="2" opacity="0.6"/>
  </svg>

  <div class="logo-tab">
    <div class="logo-name">Quellmark<br>Metalworks, LLC</div>
  </div>

  <h1 class="headline">Why Us</h1>

  <h2 class="section-title aluminum">Aluminum</h2>
  <ul class="feature-list aluminum">
    <li>6G certified in MIG and TIG</li>
    <li>Fully trained AWS/BPA certified</li>
    <li>No thinning or weakening of bus do to compression</li>
  </ul>

  <h2 class="section-title steel">Steel Welding</h2>
  <ul class="feature-list steel">
    <li>Stainless and mild steel capabilities</li>
    <li>Ability to cut, repair, patch or create projects from steel</li>
    <li>5F certified for all steel structural welding</li>
  </ul>

  <div class="diamond shop shadowed" role="img" aria-label="Welder working on an aluminum bus plate in the shop"></div>
  <div class="diamond lineman shadowed" role="img" aria-label="Field welder in high-visibility gear welding overhead bus"></div>
  <div class="diamond field" role="img" aria-label="Welder grinding a steel structure at a substation with sparks"></div>
  <div class="diamond bus-joint" role="img" aria-label="Close view of a finished aluminum weld joint"></div>

  <div class="web-pill">
    <svg width="38" height="38" viewBox="0 0 38 38" aria-hidden="true">
      <g fill="none" stroke="#0054AA" stroke-width="2.6">
        <circle cx="19" cy="19" r="16.5"/>
        <ellipse cx="19" cy="19" rx="7.5" ry="16.5"/>
        <line x1="2.5" y1="19" x2="35.5" y2="19"/>
        <line x1="5" y1="11" x2="33" y2="11"/>
        <line x1="5" y1="27" x2="33" y2="27"/>
      </g>
    </svg>
    <span>brevoforge.com</span>
  </div>
</main>
</body>
</html>
```